Gardener needs an exciting new flyer design.

I'm a passionate gardener that requires a custom flyer design for a owner operator gardening business. Design will be for a DL flyer. I'm based on the Sunshine coast in Queensland Australia. My target audience is the residential market on the Sunshine coast. Business name is Marlowe Greens. My services are, lawn mowing, weeding, Eco Friendly fertilizing, green waste removal, Mulching, tree and shrub pruning, Full garden makeovers, hedging, pressure cleaning, privacy screening, Timber deck rejuvenation, Planting, Turf preparation and installation, and much more. Free no obligation quotes, reliable and friendly service, great rates. 12 years experience. Web www.marlowegreens.com.au - Phone 0418527064 - Email doug@marlowegreens.com.au I would like the design to portray a friendly and professional approach.

Target Market(s)

Residential

Industry/Entity Type

Gardener

Font styles to use
Serif

Colors
9ccb3b
abd037
3176b5

Requirements
Must have
• my services, my logo, my contact details,

```html
<!DOCTYPE html>
<html lang="en">
<head>
<meta charset="utf-8">
<title>Marlowe Greens – DL Flyer</title>
<link rel="stylesheet" href="https://fonts.googleapis.com/css2?family=Playfair+Display:wght@500;700&family=Roboto:wght@500;700&display=swap">
<style>
  :root {
    --page-bg: #6cb548;
    --grass-dark: #1f4a1e;
    --grass-mid: #2f6a2a;
    --brand-green: #2e8b3a;
    --band-green: #238a3a;
    --tick-green: #5cb630;
    --paper: #ebebeb;
    --ink: #161616;
    --line: #2a2a2a;
    --white: #ffffff;
    --contact-ink: #eef6ea;
  }
  * { box-sizing: border-box; margin: 0; padding: 0; }
  html, body { width: 1121px; height: 1200px; overflow: hidden; }
  body { background: var(--page-bg); position: relative; font-family: "Roboto", Arial, sans-serif; }

  .flyer {
    position: absolute; left: 301px; top: 50px;
    width: 452px; height: 960px;
    transform: scale(1.146); transform-origin: top left;
    background: var(--paper);
    box-shadow: 0 18px 40px rgba(0,0,0,.28);
    overflow: hidden;
  }

  .hero { position: absolute; left: 0; top: 0; width: 452px; height: 336px; }
  .hero-grass {
    position: absolute; inset: 0;
    background: radial-gradient(ellipse at 50% 40%, var(--grass-mid), var(--grass-dark));
  }
  .brand-disc {
    position: absolute; left: 95px; top: 42px; width: 260px; height: 260px;
    border-radius: 50%; background: var(--paper);
    display: flex; align-items: center; justify-content: center;
  }
  .brand-name {
    font-family: "Playfair Display", Georgia, serif; font-weight: 700;
    font-size: 27px; color: var(--brand-green);
  }

  .services-title {
    position: absolute; left: 0; top: 336px; width: 452px; height: 71px;
    display: flex; align-items: center; justify-content: center;
    font-family: "Playfair Display", Georgia, serif; font-weight: 500;
    font-size: 44px; letter-spacing: 27px; padding-left: 27px; color: var(--ink);
  }

  .services-grid {
    position: absolute; left: 0; top: 407px; width: 452px; height: 286px;
    display: grid; grid-template-columns: 165px 118px 169px; grid-template-rows: repeat(5, 1fr);
    border-top: 2px solid var(--line); border-bottom: 2px solid var(--line);
  }
  .service {
    display: flex; align-items: center; gap: 8px; padding-left: 22px;
    font-size: 12.5px; font-weight: 500; letter-spacing: 1px; line-height: 1.25;
    text-transform: uppercase; color: var(--ink);
    border-bottom: 2px solid var(--line);
  }
  .service:nth-last-child(-n+3) { border-bottom: none; }
  .service:nth-child(3n+1), .service:nth-child(3n+2) { border-right: 2px solid var(--line); }
  .service:nth-child(3n+2), .service:nth-child(3n) { padding-left: 10px; }
  .tick { width: 20px; height: 12px; flex: none; }

  .promise {
    position: absolute; left: 0; top: 693px; width: 452px; height: 109px;
    display: flex; align-items: center; gap: 20px; padding-left: 30px;
  }
  .promise-mark {
    width: 72px; font-family: "Playfair Display", Georgia, serif; font-weight: 700;
    font-size: 15px; line-height: 1.1; color: var(--brand-green); text-align: center;
  }
  .promise-list { list-style: none; font-weight: 700; font-size: 21px; line-height: 27px; color: var(--ink); }

  .experience {
    position: absolute; left: 0; top: 802px; width: 452px; height: 46px;
    background: linear-gradient(180deg, var(--grass-mid), var(--grass-dark));
    display: flex; align-items: center; justify-content: center;
    color: var(--white); font-weight: 700; font-size: 28px; letter-spacing: 3px;
  }
  .contact {
    position: absolute; left: 0; top: 848px; width: 452px; height: 112px;
    background: var(--band-green); color: var(--contact-ink);
    display: flex; flex-direction: column; align-items: center; justify-content: center;
    font-weight: 500; font-size: 21px; line-height: 26px;
  }
</style>
</head>
<body>
  <main class="flyer">
    <header class="hero">
      <div class="hero-grass" role="img" aria-label="Close-up texture of green lawn grass with soft leaf shapes"></div>
      <div class="brand-disc"><span class="brand-name">Marlowe Greens</span></div>
    </header>

    <h1 class="services-title">SERVICES</h1>

    <section class="services-grid">
      <div class="service"><svg class="tick" viewBox="0 0 20 12"><path d="M1 6 L7 11 L19 1" fill="none" stroke="var(--tick-green)" stroke-width="3"/></svg><span>Lawn<br>Mowing</span></div>
      <div class="service"><svg class="tick" viewBox="0 0 20 12"><path d="M1 6 L7 11 L19 1" fill="none" stroke="var(--tick-green)" stroke-width="3"/></svg><span>Weeding</span></div>
      <div class="service"><svg class="tick" viewBox="0 0 20 12"><path d="M1 6 L7 11 L19 1" fill="none" stroke="var(--tick-green)" stroke-width="3"/></svg><span>Green Waste<br>Removal</span></div>
      <div class="service"><svg class="tick" viewBox="0 0 20 12"><path d="M1 6 L7 11 L19 1" fill="none" stroke="var(--tick-green)" stroke-width="3"/></svg><span>Privacy<br>Screening</span></div>
      <div class="service"><svg class="tick" viewBox="0 0 20 12"><path d="M1 6 L7 11 L19 1" fill="none" stroke="var(--tick-green)" stroke-width="3"/></svg><span>Mulching</span></div>
      <div class="service"><svg class="tick" viewBox="0 0 20 12"><path d="M1 6 L7 11 L19 1" fill="none" stroke="var(--tick-green)" stroke-width="3"/></svg><span>Tree and<br>Shrub</span></div>
      <div class="service"><svg class="tick" viewBox="0 0 20 12"><path d="M1 6 L7 11 L19 1" fill="none" stroke="var(--tick-green)" stroke-width="3"/></svg><span>Full Garden<br>Makeovers</span></div>
      <div class="service"><svg class="tick" viewBox="0 0 20 12"><path d="M1 6 L7 11 L19 1" fill="none" stroke="var(--tick-green)" stroke-width="3"/></svg><span>Pruning</span></div>
      <div class="service"><svg class="tick" viewBox="0 0 20 12"><path d="M1 6 L7 11 L19 1" fill="none" stroke="var(--tick-green)" stroke-width="3"/></svg><span>Timber Deck<br>Rejuvenation</span></div>
      <div class="service"><svg class="tick" viewBox="0 0 20 12"><path d="M1 6 L7 11 L19 1" fill="none" stroke="var(--tick-green)" stroke-width="3"/></svg><span>Turf<br>Preparation</span></div>
      <div class="service"><svg class="tick" viewBox="0 0 20 12"><path d="M1 6 L7 11 L19 1" fill="none" stroke="var(--tick-green)" stroke-width="3"/></svg><span>Hedging</span></div>
      <div class="service"><svg class="tick" viewBox="0 0 20 12"><path d="M1 6 L7 11 L19 1" fill="none" stroke="var(--tick-green)" stroke-width="3"/></svg><span>Pressure<br>Cleaning</span></div>
      <div class="service"><svg class="tick" viewBox="0 0 20 12"><path d="M1 6 L7 11 L19 1" fill="none" stroke="var(--tick-green)" stroke-width="3"/></svg><span>Eco Friendly<br>Fertilizing</span></div>
      <div class="service"><svg class="tick" viewBox="0 0 20 12"><path d="M1 6 L7 11 L19 1" fill="none" stroke="var(--tick-green)" stroke-width="3"/></svg><span>Planting</span></div>
      <div class="service"><svg class="tick" viewBox="0 0 20 12"><path d="M1 6 L7 11 L19 1" fill="none" stroke="var(--tick-green)" stroke-width="3"/></svg><span>Installation<br>&amp; Much More</span></div>
    </section>

    <section class="promise">
      <div class="promise-mark">Marlowe Greens</div>
      <ul class="promise-list">
        <li>Free No Obligation Quotes</li>
        <li>Reliable And Friendly Service</li>
        <li>Great Rates</li>
      </ul>
    </section>

    <div class="experience">12 YEARS EXPERIENCE</div>

    <footer class="contact">
      <span>0418 527 064</span>
      <span>www.marlowegreens.com.au</span>
      <span>doug@marlowegreens.com.au</span>
    </footer>
  </main>
</body>
</html>
```